Velmar Corsa 340 mid roof wrap for remodeling company

I think most car wraps are tacky. I want to keep it simple and clean. No full wraps, it should be a partial wrap, and I want the main color to be white.

Black and white is best, but if adding one or two more colors would work best, we can do that. Gray would be the first choice, and maybe one more like red or blue if needed.

I included a photo of the blank van photos with my logos superimposed in the way I have them on my current vehicle. I do want to keep the same fonts, info, and arrow logo.

```html
<!DOCTYPE html>
<html lang="en">
<head>
<meta charset="utf-8">
<title>Brightline Homes – Velmar Corsa 340 Partial Wrap</title>
<link href="https://fonts.googleapis.com/css2?family=Lato:wght@400;700;900&family=Open+Sans:wght@600;700&display=swap" rel="stylesheet">
<style>
  :root {
    --backdrop: #1a1617;
    --body-white: #f1f1f1;
    --ink: #141414;
    --mark-grey: #6e6e6e;
    --band-red: #d9534d;
    --band-red-deep: #c13c3a;
    --band-blue: #3fa3cb;
    --band-blue-light: #5cb6d8;
    --band-text: #ffffff;
  }
  * { margin: 0; padding: 0; box-sizing: border-box; }
  html, body { width: 1200px; height: 1094px; overflow: hidden; background: var(--backdrop); }
  .canvas { position: relative; width: 1200px; height: 1094px; font-family: "Lato", sans-serif; color: var(--ink); }

  .surface { position: absolute; background: var(--body-white); }
  .surface--side { left: 120px; top: 145px; width: 950px; height: 330px; border-radius: 60px 30px 14px 14px; }
  .surface--front { left: 195px; top: 665px; width: 330px; height: 300px; border-radius: 40px 40px 18px 18px; }
  .surface--rear { left: 690px; top: 655px; width: 310px; height: 270px; border-radius: 30px 30px 12px 12px; }

  .abs { position: absolute; white-space: nowrap; }

  .brand-square { position: absolute; background: var(--mark-grey); }
  .brand-name { font-weight: 700; color: var(--ink); }

  /* side */
  .side-square { left: 600px; top: 212px; width: 48px; height: 48px; }
  .side-name-1 { left: 698px; top: 200px; font-size: 33px; letter-spacing: 9px; }
  .side-name-2 { left: 698px; top: 238px; font-size: 25px; letter-spacing: 10px; }
  .side-service { left: 574px; top: 284px; font-size: 20px; font-weight: 900; letter-spacing: 5.2px; }
  .side-band { left: 482px; top: 326px; }
  .side-phone { left: 683px; top: 368px; font-size: 19px; font-weight: 900; letter-spacing: 2px; }
  .side-license { left: 320px; top: 377px; font-size: 7px; letter-spacing: 2.4px; }
  .side-dot { position: absolute; left: 444px; top: 379px; width: 7px; height: 7px; border-radius: 50%; background: #333; }

  .band-text { font-family: "Open Sans", sans-serif; font-weight: 700; fill: var(--band-text); letter-spacing: 2px; }

  /* front */
  .front-square { left: 349px; top: 816px; width: 22px; height: 22px; }
  .front-name { left: 262px; top: 838px; font-size: 8px; letter-spacing: 7.5px; }

  /* rear */
  .rear-square { left: 822px; top: 700px; width: 46px; height: 46px; }
  .rear-name { left: 845px; top: 765px; transform: translateX(-50%); font-size: 16px; letter-spacing: 5px; }
  .rear-service { left: 845px; top: 785px; transform: translateX(-50%); font-size: 10px; font-weight: 900; letter-spacing: 2.2px; }
  .rear-band { left: 742px; top: 805px; }
  .rear-phone { left: 845px; top: 876px; transform: translateX(-50%); font-size: 18px; font-weight: 900; letter-spacing: 2px; }
  .rear-license { left: 713px; top: 908px; font-size: 6.5px; letter-spacing: 2.2px; }
</style>
</head>
<body>
<main class="canvas">

  <section class="wrap-side" aria-label="Side panel layout">
    <div class="surface surface--side"></div>
    <div class="brand-square side-square"></div>
    <div class="abs brand-name side-name-1">BRIGHTLINE</div>
    <div class="abs brand-name side-name-2">HOMES</div>
    <div class="abs side-service">RESIDENTAL REMODELING</div>
    <svg class="abs side-band" width="532" height="28" viewBox="0 0 532 28">
      <defs>
        <linearGradient id="side-red" x1="0" x2="1"><stop offset="0" stop-color="var(--band-red)"/><stop offset="1" stop-color="var(--band-red-deep)"/></linearGradient>
        <linearGradient id="side-blue" x1="0" x2="1"><stop offset="0" stop-color="var(--band-blue)"/><stop offset="1" stop-color="var(--band-blue-light)"/></linearGradient>
      </defs>
      <polygon points="18,0 280,0 302,27 0,27" fill="url(#side-red)"/>
      <polygon points="278,0 530,0 506,27 300,27" fill="url(#side-blue)"/>
      <text class="band-text" x="165" y="19" font-size="13" text-anchor="middle">BRIGHTLINEHOMESCT.COM</text>
      <text class="band-text" x="400" y="19" font-size="13" text-anchor="middle">EASTBROOK, CT</text>
    </svg>
    <div class="abs side-phone">(555)-014-7362</div>
    <div class="abs side-license">LICENSE#HIC.0517284</div>
    <div class="side-dot"></div>
  </section>

  <section class="wrap-front" aria-label="Front hood layout">
    <div class="surface surface--front"></div>
    <div class="brand-square front-square"></div>
    <div class="abs brand-name front-name">BRIGHTLINE HOMES</div>
  </section>

  <section class="wrap-rear" aria-label="Rear door layout">
    <div class="surface surface--rear"></div>
    <div class="brand-square rear-square"></div>
    <div class="abs brand-name rear-name">BRIGHTLINE HOMES</div>
    <div class="abs rear-service">RESIDENTIAL REMODELING</div>
    <svg class="abs rear-band" width="222" height="42" viewBox="0 0 222 42">
      <defs>
        <linearGradient id="rear-blue" x1="0" x2="1"><stop offset="0" stop-color="var(--band-blue)"/><stop offset="1" stop-color="var(--band-blue-light)"/></linearGradient>
      </defs>
      <polygon points="10,0 212,0 222,20 0,20" fill="var(--band-red-deep)"/>
      <polygon points="16,20 206,20 190,40 32,40" fill="url(#rear-blue)"/>
      <text class="band-text" x="111" y="15" font-size="10.5" text-anchor="middle">BRIGHTLINEHOMESCT.COM</text>
      <text class="band-text" x="111" y="34" font-size="8.5" text-anchor="middle" style="letter-spacing:1.5px">EASTBROOK, CT</text>
    </svg>
    <div class="abs rear-phone">(555)-014-7362</div>
    <div class="abs rear-license">LICENSE#HIC.0517284</div>
  </section>

</main>
</body>
</html>
```